Frostwyn.co - Polar Expeditions Specialists

We need a modern, visually striking business card for Frostwyn.co, a company specialized in selling expedition cruises to the most remote regions on Earth, with a focus on the Arctic and Antarctica. The design should instantly communicate that the cardholder is an expert in polar travel. Use clean, premium aesthetics with cool tones like icy blue and white, possibly incorporating polar imagery (ice, glaciers, penguins, etc.)

Attached the logo

Contact Information for Business Card

Feels high-end and trustworthy.. Visually memorable — encourages people to keep it

Colors
0054AA
0677BA
7BADD7
CADEEF
E8F1F8

Requirements
Must have
• ice, glaciers, penguins, montains
Nice to have
• modern, transparente,

```html
<!DOCTYPE html>
<html lang="en">
<head>
<meta charset="utf-8">
<title>Frostwyn.co – Business Card</title>
<link href="https://fonts.googleapis.com/css2?family=Poppins:wght@400;500;600;700&display=swap" rel="stylesheet">
<style>
  :root {
    --backdrop: #3d3d3d;
    --brand-blue: #3674b5;
    --ice-blue: #7badd7;
    --frost: #cadeef;
    --snow: #ffffff;
    --card-radius: 22px;
  }
  * { box-sizing: border-box; margin: 0; padding: 0; }
  html, body {
    width: 1200px;
    height: 803px;
    overflow: hidden;
    background: var(--backdrop);
    font-family: "Poppins", sans-serif;
  }
  .card-set {
    position: relative;
    width: 1200px;
    height: 803px;
  }
  .card {
    position: absolute;
    top: 251px;
    width: 520px;
    height: 300px;
    border-radius: var(--card-radius);
    overflow: hidden;
    box-shadow: 0 18px 40px rgba(0, 0, 0, 0.35);
  }
  /* Front side */
  .card--front {
    left: 60px;
    background: var(--brand-blue);
    color: var(--snow);
  }
  .polar-artwork {
    position: absolute;
    right: 0;
    top: 0;
    width: 270px;
    height: 300px;
    background: linear-gradient(160deg, var(--snow) 0%, var(--frost) 55%, var(--ice-blue) 100%);
    opacity: 0.9;
    border-radius: 140px 0 0 0;
  }
  .front-content {
    position: absolute;
    left: 34px;
    top: 30px;
    width: 230px;
  }
  .brand-name {
    font-weight: 700;
    font-size: 36px;
    line-height: 1;
    letter-spacing: -0.5px;
  }
  .brand-tagline {
    font-weight: 500;
    font-size: 10.5px;
    margin-top: 5px;
  }
  .holder-name {
    font-weight: 600;
    font-size: 19px;
    margin-top: 22px;
    line-height: 1.1;
  }
  .holder-role {
    font-weight: 400;
    font-size: 11px;
    opacity: 0.9;
  }
  .address {
    font-size: 11px;
    line-height: 1.35;
    margin-top: 14px;
  }
  .contact-list {
    list-style: none;
    margin-top: 8px;
    font-size: 11px;
    line-height: 1.45;
  }
  .contact-list li {
    display: flex;
    align-items: center;
    gap: 7px;
  }
  .contact-icon {
    width: 10px;
    height: 10px;
    flex: none;
  }
  /* Back side */
  .card--back {
    left: 620px;
    background: var(--snow);
    color: var(--brand-blue);
  }
  .back-lockup {
    position: absolute;
    left: 50%;
    top: 50%;
    transform: translate(-50%, -50%);
    display: flex;
    align-items: center;
    gap: 16px;
  }
  .lockup-dot {
    width: 58px;
    height: 58px;
    border-radius: 50%;
    background: var(--brand-blue);
    flex: none;
  }
  .back-name {
    font-weight: 700;
    font-size: 50px;
    line-height: 1;
    letter-spacing: -0.5px;
  }
  .back-tagline {
    font-weight: 500;
    font-size: 14px;
    margin-top: 6px;
  }
</style>
</head>
<body>
  <main class="card-set">
    <section class="card card--front">
      <div class="polar-artwork" role="img" aria-label="White silhouette of a polar bear with two penguins on an ice ledge, with small stars"></div>
      <div class="front-content">
        <h1 class="brand-name">Frostwyn.co</h1>
        <p class="brand-tagline">Polar Expeditions Specialists</p>
        <h2 class="holder-name">Elias Marrow</h2>
        <p class="holder-role">President</p>
        <p class="address">4120 Birchwood Way<br>Halden Bay, Norland 58210</p>
        <ul class="contact-list">
          <li>
            <svg class="contact-icon" viewBox="0 0 10 10" aria-hidden="true"><path d="M2 0.8 L3.6 2.8 L2.8 3.8 Q4 6.2 6.2 7.2 L7.2 6.4 L9.2 8 L8 9.4 Q3.5 9 0.6 2 Z" fill="currentColor"/></svg>
            555-210-4817
          </li>
          <li>
            <svg class="contact-icon" viewBox="0 0 10 10" aria-hidden="true"><rect x="2.2" y="0.6" width="5.6" height="8.8" rx="1" fill="none" stroke="currentColor" stroke-width="1"/></svg>
            555-382-9061
          </li>
          <li>
            <svg class="contact-icon" viewBox="0 0 10 10" aria-hidden="true"><rect x="0.5" y="2" width="9" height="6.2" fill="currentColor"/><path d="M0.8 2.3 L5 5.6 L9.2 2.3" fill="none" stroke="#3674b5" stroke-width="0.9"/></svg>
            info@frostwyn.com
          </li>
          <li>
            <svg class="contact-icon" viewBox="0 0 10 10" aria-hidden="true"><circle cx="5" cy="5" r="4.4" fill="none" stroke="currentColor" stroke-width="1"/><ellipse cx="5" cy="5" rx="1.8" ry="4.4" fill="none" stroke="currentColor" stroke-width="0.8"/><line x1="0.6" y1="5" x2="9.4" y2="5" stroke="currentColor" stroke-width="0.8"/></svg>
            www.frostwyn.com
          </li>
        </ul>
      </div>
    </section>

    <section class="card card--back">
      <div class="back-lockup">
        <span class="lockup-dot" aria-hidden="true"></span>
        <div>
          <p class="back-name">Frostwyn.co</p>
          <p class="back-tagline">Polar Expeditions Specialists</p>
        </div>
      </div>
    </section>
  </main>
</body>
</html>
```